TRV Business Card

Business card design for a handyman company. Want to portray a professional image and stay away from the "Mom & Pops" image that is normally associated with handyman companies.

Business

```html
<!DOCTYPE html>
<html lang="en">
<head>
<meta charset="utf-8">
<title>TRV Business Card</title>
<link rel="stylesheet" href="https://fonts.googleapis.com/css2?family=Noto+Serif:ital@0;1&family=Open+Sans:wght@400;600;700&display=swap">
<style>
  :root {
    --canvas-bg: #e6e6e8;
    --card-white: #f6f6f7;
    --brand-purple: #2f1d6e;
    --ink-navy: #1c2333;
    --ink-grey: #4a4a52;
    --list-text: #e9e6f5;
  }
  * { box-sizing: border-box; margin: 0; padding: 0; }
  html, body { width: 1200px; height: 873px; overflow: hidden; }
  body {
    background: var(--canvas-bg);
    position: relative;
    font-family: "Open Sans", sans-serif;
  }
  .card {
    position: absolute;
    top: 290px;
    width: 520px;
    height: 297px;
    background: var(--card-white);
    box-shadow: 0 6px 18px rgba(0,0,0,0.18);
    overflow: hidden;
  }
  .card--front { left: 50px; }
  .card--back {
    left: 630px;
    border: 8px solid var(--ink-navy);
    display: flex;
    align-items: center;
    justify-content: center;
  }
  .front__band {
    position: absolute;
    inset: 0;
    width: 100%;
    height: 100%;
  }
  .service-list {
    position: absolute;
    left: 34px;
    top: 26px;
    list-style: none;
    font-family: "Noto Serif", serif;
    font-size: 13px;
    line-height: 1.4;
    color: var(--list-text);
  }
  .service-list__title { font-style: italic; margin-bottom: 8px; }
  .service-list li { padding-left: 14px; }
  .brand-name {
    font-family: "Open Sans", sans-serif;
    font-weight: 700;
    color: var(--ink-navy);
    letter-spacing: 2px;
    display: flex;
    align-items: center;
    gap: 12px;
  }
  .brand-name__mark {
    width: 14px;
    height: 14px;
    background: var(--ink-navy);
  }
  .front__brand {
    position: absolute;
    left: 280px;
    top: 38px;
    font-size: 52px;
  }
  .front__email {
    position: absolute;
    left: 284px;
    top: 118px;
    font-size: 10px;
    font-weight: 600;
    letter-spacing: 1px;
    text-transform: uppercase;
    color: var(--ink-grey);
  }
  .contact {
    position: absolute;
    left: 300px;
    top: 160px;
    font-size: 13px;
    font-weight: 600;
    line-height: 1.45;
    color: var(--ink-grey);
    font-style: normal;
  }
  .contact__phones { margin-top: 14px; }
  .front__tagline {
    position: absolute;
    left: 34px;
    bottom: 22px;
    font-family: "Noto Serif", serif;
    font-size: 17px;
    color: var(--ink-grey);
  }
  .back__brand { font-size: 72px; }
</style>
</head>
<body>
  <section class="card card--front">
    <svg class="front__band" viewBox="0 0 520 297" preserveAspectRatio="none" aria-hidden="true">
      <polygon points="0,0 250,0 120,190 0,125" fill="var(--brand-purple)"/>
    </svg>
    <ul class="service-list">
      <li class="service-list__title">Potential Verbage:</li>
      <li>Home Repairs</li>
      <li>Handyman Services</li>
      <li>Drain Cleaning</li>
      <li>Carpet Cleaning</li>
    </ul>
    <div class="brand-name front__brand"><span class="brand-name__mark"></span>TRV</div>
    <p class="front__email">info@trvservices.com</p>
    <address class="contact">
      <p>4170 Harlan Ave</p>
      <p>Millbrook, Ks 66090</p>
      <p class="contact__phones">P: (555) 310-4821</p>
      <p>F: (555) 310-4822</p>
    </address>
    <p class="front__tagline">Residential and Commercial Services</p>
  </section>

  <section class="card card--back">
    <div class="brand-name back__brand"><span class="brand-name__mark"></span>TRV</div>
  </section>
</body>
</html>
```